Radiant Crossing - An Exciting Mission & Book Cover Project

Help me to inspire people to live their best life! This is a mission, not just a design project.
I need a Book Cover designed to keep me inspired on the process of writing my book.
Book Title: Radiant Crossing
Tag Line: Three Simple Steps to get out of your own way, SuperCharge your Life and Step into Purpose!
Author: Marlis Quenby

The three steps are: Ownership, Vision and Action (Not sure if this should be on the front or back of the book cover)

The book is a self-help, motivational book. Personal development.
The cover needs to be strong and capture peoples attention, especially with competing shelf space. I almost see a fire ball of flame or explosion that will grab peoples attention.
My company is The Lantern Institute. I have added the company logo and a few pages of my presentation and topic outline to give an idea.
Maybe: The Lantern Institute logo on back of the cover. website is marlisquenby.com

THOUGHT: People should be able to take a photo of them holding the book cover showing what area of life they want Radiant Crossing in. This is why the front cover must be so visual and powerful that they want to take a photo with it. Ie. Explosion, fire, strong and bold.

Target Market(s)

Anyone who feels stuck and needs to breakthrough and move forward in life.

Industry/Entity Type

Motivation

Font styles to use
Serif
Sans Serif

Colors
ec1f27
f37122
fbed22

Requirements
Must have
• The design must be STRONG, SIMPLE, STAND OUT ON BOOK SHELVES.
Must have an open file to swap the photo and copy out.

Back Cover Page
1) Summary
2) 2-3 testimonials. One sentence.
3) About the Author (maybe with photo)
4) Lantern Institute logo
5) Website: radiantcrossing.com and marlisquenby.com
Nice to have
• If my photo works somewhere that would be great. I will change the photo later.
Added Where's Your Harbor? a nice cover example.
Should not have
• Right now I am writing the summary for the back of the cover. For now use Loreum Ipsum text and 2-3 recommendations. Again, I will get these only later.

```html
<!DOCTYPE html>
<html lang="en">
<head>
<meta charset="utf-8">
<title>Radiant Crossing – Book Cover</title>
<link rel="stylesheet" href="https://fonts.googleapis.com/css2?family=Oswald:wght@500;700&family=Anton&family=Libre+Baskerville:ital,wght@0,400;0,700;1,400&display=swap">
<style>
  :root {
    --red: #ec1f27;
    --orange: #f37122;
    --yellow: #fbed22;
    --black: #0b0b0b;
    --white: #ffffff;
    --paper: #f4f4f4;
    --ink: #111111;
    --flame-deep: #b8230f;
    --flame-mid: #f0661c;
    --flame-light: #ffc04a;
    --shard: #9aa3a6;
  }
  * { box-sizing: border-box; margin: 0; padding: 0; }
  html, body { width: 1200px; height: 800px; overflow: hidden; }
  body { background: var(--paper); font-family: "Libre Baskerville", Georgia, serif; }

  .cover-spread {
    position: absolute; left: 175px; top: 100px;
    width: 850px; height: 600px;
    display: flex;
    box-shadow: 0 10px 30px rgba(0,0,0,.18);
  }

  /* ---------- Back cover ---------- */
  .back-cover {
    position: relative; width: 400px; height: 600px;
    background: linear-gradient(90deg, var(--red) 0%, var(--red) 62%, #5a0c0f 88%, var(--black) 100%);
    color: var(--white);
  }
  .back-summary {
    background: var(--black);
    height: 180px; padding: 34px 28px 0 28px;
    font-size: 12.5px; line-height: 1.45;
  }
  .testimonials { padding: 26px 28px 0 28px; }
  .testimonial { font-size: 11.5px; line-height: 1.45; margin-bottom: 16px; }
  .testimonial cite { font-style: italic; }
  .author-block { display: flex; gap: 12px; padding: 8px 28px 0 28px; }
  .author-photo {
    width: 92px; height: 92px; flex: none;
    background: var(--yellow); position: relative; overflow: hidden;
  }
  .author-photo .photo-fill {
    position: absolute; inset: 10px 14px 0 14px;
    background: linear-gradient(180deg, #c9b9a8 0%, #2b3550 65%, #1c2338 100%);
  }
  .author-bio { font-size: 11px; line-height: 1.5; }
  .publisher-mark {
    position: absolute; left: 28px; bottom: 58px;
    display: flex; align-items: center; gap: 8px;
    font-family: "Oswald", Arial, sans-serif; font-weight: 500;
    font-size: 11px; letter-spacing: .06em; text-transform: uppercase; color: var(--white);
  }
  .publisher-mark .dot { width: 10px; height: 10px; border-radius: 50%; background: var(--white); }

  /* ---------- Spine ---------- */
  .spine {
    width: 50px; height: 600px; background: var(--orange);
    display: flex; align-items: center; justify-content: center;
  }
  .spine-text {
    writing-mode: vertical-rl;
    display: flex; align-items: center; gap: 26px;
    color: var(--ink); white-space: nowrap;
  }
  .spine-author { font-family: "Libre Baskerville", Georgia, serif; font-style: italic; font-size: 17px; letter-spacing: .08em; }
  .spine-title { font-family: "Anton", "Oswald", sans-serif; font-size: 19px; letter-spacing: .12em; text-transform: uppercase; }

  /* ---------- Front cover ---------- */
  .front-cover {
    position: relative; width: 400px; height: 600px;
    background: var(--white); overflow: hidden;
  }
  .front-header {
    height: 230px; background: var(--black);
    padding: 48px 0 0 22px;
  }
  .title-main {
    font-family: "Anton", "Oswald", sans-serif; color: var(--red);
    font-size: 68px; line-height: 1; letter-spacing: .01em; text-transform: uppercase;
  }
  .title-sub {
    font-family: "Oswald", Arial, sans-serif; font-weight: 700; color: var(--orange);
    font-size: 40px; line-height: 1.1; letter-spacing: .02em; text-transform: uppercase;
    margin-left: 38px;
  }
  .hero-art {
    position: absolute; left: 150px; top: 170px; width: 250px; height: 300px;
    background: radial-gradient(ellipse at 45% 52%, var(--flame-light) 0%, var(--flame-mid) 32%, var(--flame-deep) 55%, rgba(154,163,166,.55) 72%, rgba(255,255,255,0) 86%);
  }
  .tagline {
    position: absolute; left: 20px; top: 290px; width: 175px;
    font-family: "Oswald", Arial, sans-serif; font-weight: 700;
    line-height: 1.12; color: var(--ink);
  }
  .tagline .lead { color: var(--red); font-size: 24px; display: block; }
  .tagline .small { font-size: 15px; display: block; }
  .tagline .accent-orange { color: var(--orange); font-size: 22px; }
  .tagline .accent-red { color: var(--red); font-size: 26px; }
  .tagline .small-inline { font-size: 15px; }
  .front-footer {
    position: absolute; left: 0; bottom: 0; width: 100%; height: 56px;
    background: var(--yellow);
    display: flex; align-items: center; justify-content: center;
    font-family: "Libre Baskerville", Georgia, serif; font-size: 17px;
    letter-spacing: .12em; color: var(--ink);
  }
</style>
</head>
<body>
  <main class="cover-spread">
    <section class="back-cover">
      <p class="back-summary">Lorem ipsum dolor sit amet, consectetur adipiscing elit, sed do eiusmod tempor incididunt ut labore et dolore magna aliqua. Ut enim ad minim veniam, quis nostrud exercitation ullamco laboris nisi.</p>
      <div class="testimonials">
        <p class="testimonial">“This book is very inspiring and straight forward, goal setting in the easiest form” <cite>Tobin Marsh</cite></p>
        <p class="testimonial">“This book is very inspiring and straight forward, goal setting in the easiest form” <cite>Tobin Marsh</cite></p>
        <p class="testimonial">“This book is very inspiring and straight forward, goal setting in the easiest form” <cite>Tobin Marsh</cite></p>
      </div>
      <div class="author-block">
        <div class="author-photo"><div class="photo-fill" role="img" aria-label="Portrait photo of the author in a dark suit"></div></div>
        <p class="author-bio">Lorem ipsum dolor sit amet, consectetur adipiscing elit. Sed do eiusmod tempor incididunt ut labore et dolore magna aliqua, ut enim ad minim veniam.</p>
      </div>
      <div class="publisher-mark"><span class="dot"></span>The Lantern Institute</div>
    </section>

    <section class="spine">
      <div class="spine-text">
        <span class="spine-author">Marlis Quenby</span>
        <span class="spine-title">Radiant Crossing</span>
      </div>
    </section>

    <section class="front-cover">
      <header class="front-header">
        <h1 class="title-main">Radiant</h1>
        <h2 class="title-sub">Crossing</h2>
      </header>
      <div class="hero-art" role="img" aria-label="Flaming fist bursting through shattering glass"></div>
      <p class="tagline">
        <span class="lead">Three</span>
        <span class="small">Simple Steps</span>
        <span class="small">to get out of</span>
        <span class="accent-orange">your own way,</span><br>
        <span class="accent-red">SuperCharge</span><br>
        <span class="accent-orange">your Life</span> <span class="small-inline">and</span><br>
        <span class="accent-red">Step into Purpose!</span>
      </p>
      <footer class="front-footer">Marlis Quenby</footer>
    </section>
  </main>
</body>
</html>
```